Business Card for Quillmark Ledger - A cannabis publication for executives.

I'd like some business cards for Quillmark Ledger. The logo is done (great job!) and I need a card design I will use with PRINTLY. I made it a short project to allow time for printing before an event. These will be standard sized cards (final artwork size 3.66" x 2.16" at 300dpi) with a final card size of 3.5" x 2.0". (See PRINTLY.com if you need more info.) I might try rounded corners but am not sure yet. I think the design will work okay with rounded.

Quillmark Ledger will be a bi-weekly publication for the cannabis industry. It is targeted to investors and industry executives, not consumers or pot smokers. So our market is more B2B. However I am open to creativity and making the card something people remark on.

My contact for card:

Dana Merrow
Founder/CEO
dana@quillmarkledger.example

2740 Harlow Avenue
Boston MA 02135
(617)555-0194

Target Market(s)

Executives, Industry people and investors in the Cannabis sector.

Contact Information for Business Card

PRINTLY does do double sided and the second side can be the same or different images. Only one side is required but use of the second side would be a bonus.

Font styles to use
Serif
Sans Serif
Decorative

Colors

Designer to choose colors to be used in the design.

Requirements
Must have
• Logo, contact info
Nice to have
• Style and design to make the card stand out in a crowd.

```html
<!DOCTYPE html>
<html lang="en">
<head>
<meta charset="utf-8">
<title>Quillmark Ledger — Business Card</title>
<link rel="stylesheet" href="https://fonts.googleapis.com/css2?family=Arimo:wght@400;700&display=swap">
<style>
  :root {
    --brand-blue: #2a80f5;
    --brand-green: #72d400;
    --paper: #ffffff;
  }
  html, body {
    margin: 0;
    padding: 0;
    width: 1200px;
    height: 729px;
    overflow: hidden;
    background: var(--paper);
  }
  .card {
    position: relative;
    width: 1200px;
    height: 729px;
    background: var(--paper);
    font-family: "Arimo", Helvetica, Arial, sans-serif;
    color: var(--brand-blue);
  }
  .brand {
    position: absolute;
    left: 129px;
    top: 138px;
    display: flex;
    align-items: center;
    gap: 14px;
  }
  .brand-dot {
    width: 30px;
    height: 30px;
    border-radius: 50%;
    background: var(--brand-green);
  }
  .brand-name {
    font-size: 40px;
    font-weight: 400;
    color: var(--brand-blue);
    letter-spacing: 0.2px;
  }
  .contact-name {
    position: absolute;
    left: 129px;
    top: 244px;
    margin: 0;
    font-size: 38px;
    font-weight: 700;
    line-height: 1;
  }
  .contact-title {
    position: absolute;
    left: 129px;
    top: 295px;
    margin: 0;
    font-size: 31px;
    font-weight: 400;
    line-height: 1;
  }
  .address {
    position: absolute;
    left: 129px;
    top: 378px;
    margin: 0;
    font-style: normal;
    font-size: 31px;
    line-height: 42px;
  }
  .reach {
    position: absolute;
    left: 129px;
    top: 500px;
    margin: 0;
    padding: 0;
    list-style: none;
    font-size: 31px;
    line-height: 42px;
  }
  .reach li {
    display: flex;
    align-items: center;
    gap: 16px;
  }
  .reach svg {
    width: 38px;
    height: 28px;
    flex: none;
  }
  .symbol-field {
    position: absolute;
    left: 680px;
    top: 75px;
    width: 520px;
    height: 635px;
    border-radius: 24px 0 0 24px;
    background: linear-gradient(150deg, var(--brand-green) 0%, #9be04a 45%, var(--brand-blue) 100%);
  }
</style>
</head>
<body>
  <main class="card">
    <div class="brand">
      <span class="brand-dot"></span>
      <span class="brand-name">Quillmark Ledger</span>
    </div>

    <h1 class="contact-name">Dana Merrow</h1>
    <p class="contact-title">Founder/CEO</p>

    <address class="address">2740 Harlow Avenue<br>Boston MA 02135</address>

    <ul class="reach">
      <li>
        <svg viewBox="0 0 38 28" aria-hidden="true">
          <path d="M4 10 Q19 -2 34 10 L31 14 L25 12 L25 9 Q19 6 13 9 L13 12 L7 14 Z" fill="none" stroke="var(--brand-green)" stroke-width="2"/>
          <path d="M10 14 L28 14 L33 26 L5 26 Z" fill="none" stroke="var(--brand-green)" stroke-width="2"/>
          <circle cx="19" cy="20" r="3" fill="none" stroke="var(--brand-green)" stroke-width="2"/>
        </svg>
        <span>: (617)555-0194</span>
      </li>
      <li>
        <svg viewBox="0 0 38 28" aria-hidden="true">
          <rect x="2" y="4" width="34" height="22" fill="none" stroke="var(--brand-green)" stroke-width="2"/>
          <path d="M2 4 L19 17 L36 4 M2 26 L15 14 M36 26 L23 14" fill="none" stroke="var(--brand-green)" stroke-width="2"/>
        </svg>
        <span>: dana@quillmarkledger.example</span>
      </li>
    </ul>

    <div class="symbol-field" role="img" aria-label="Large brand symbol in green and blue"></div>
  </main>
</body>
</html>
```